Civil engineering company | Billboard

We need a billboard design for Velmora- civil engineering company. We want big logo in the center of billboard and web site (www.velmora.hr) below the logo. Also, we want an subtle abstract pattern in the background. Dimensions of the billboard are: width :10 m, height: 2m. Design must be celan and modern.
Industry/Entity Type
Civil engineering
Font styles to use
Sans Serif
Colors
F0912C
F2A743
F7CA91
FBE8D2
FDF5EE
Requirements
Must have
- Logo and new unique pattern design for Velomra company
Should not have
- pictures of construction machinery and tools

```html
<!DOCTYPE html>
<html lang="hr">
<head>
<meta charset="utf-8">
<title>Velmora – billboard</title>
<link rel="stylesheet" href="https://fonts.googleapis.com/css2?family=Questrial&family=Montserrat:wght@600&family=Open+Sans:wght@700&display=swap">
<style>
  :root {
    --page: #e4e8ec;
    --panel: #f4f4f4;
    --orange: #f0912c;
    --orange-deep: #d9731c;
    --orange-light: #f2a743;
    --pattern-light: #f6f6f6;
    --pattern-mid: #d2d2d2;
    --pattern-shade: #bdbdbd;
    --charcoal: #4a4a4a;
    --dark-wedge: #505050;
    --rule: #c4c4c4;
  }
  * { margin: 0; padding: 0; box-sizing: border-box; }
  html, body {
    width: 1200px;
    height: 1117px;
    overflow: hidden;
    background: var(--page);
  }
  .billboard {
    position: absolute;
    left: 40px;
    top: 446px;
    width: 1120px;
    height: 224px;
    background: var(--panel);
    box-shadow: 0 6px 24px rgba(0, 0, 0, 0.15);
    overflow: hidden;
  }
  .billboard__art {
    position: absolute;
    inset: 0;
    width: 100%;
    height: 100%;
  }
  .billboard__content {
    position: absolute;
    left: 377px;
    top: 0;
    width: 320px;
    height: 224px;
    display: flex;
    flex-direction: column;
    align-items: center;
    justify-content: center;
  }
  .brand {
    display: flex;
    flex-direction: column;
    align-items: center;
    gap: 8px;
  }
  .brand__square {
    width: 46px;
    height: 46px;
    border: 3px solid var(--charcoal);
  }
  .brand__name {
    font-family: "Questrial", sans-serif;
    font-size: 42px;
    line-height: 1;
    letter-spacing: 1px;
    text-transform: uppercase;
    color: var(--orange);
  }
  .tagline {
    margin-top: 6px;
    font-family: "Montserrat", sans-serif;
    font-weight: 600;
    font-size: 9.5px;
    letter-spacing: 0.3px;
    color: var(--charcoal);
    text-transform: uppercase;
    white-space: nowrap;
  }
  .divider {
    margin-top: 9px;
    width: 270px;
    height: 1px;
    background: var(--rule);
  }
  .website {
    margin-top: 8px;
    font-family: "Open Sans", sans-serif;
    font-weight: 700;
    font-size: 22px;
    line-height: 1.1;
    color: var(--charcoal);
  }
</style>
</head>
<body>
  <div class="billboard">
    <svg class="billboard__art" viewBox="0 0 1000 200" preserveAspectRatio="none">
      <defs>
        <linearGradient id="pattern-tone" x1="0" y1="0" x2="1" y2="1">
          <stop offset="0" stop-color="var(--pattern-mid)"/>
          <stop offset="0.35" stop-color="var(--pattern-light)"/>
          <stop offset="0.7" stop-color="var(--pattern-mid)"/>
          <stop offset="1" stop-color="var(--pattern-shade)"/>
        </linearGradient>
        <linearGradient id="band-tone" x1="0" y1="0" x2="0" y2="1">
          <stop offset="0" stop-color="var(--orange-deep)"/>
          <stop offset="0.5" stop-color="var(--orange)"/>
          <stop offset="1" stop-color="var(--orange-light)"/>
        </linearGradient>
      </defs>
      <polygon class="pattern pattern--left" role="img" aria-label="Subtle abstract background pattern of embossed light-grey geometric squares"
               points="0,0 166,0 300,200 0,200" fill="url(#pattern-tone)"/>
      <polygon class="wedge wedge--left" points="0,105 0,200 85,200" fill="var(--dark-wedge)"/>
      <polygon class="band band--left" points="166,0 309,0 356,200 300,200" fill="url(#band-tone)"/>
      <polygon class="band-shade band-shade--left" points="250,0 309,0 330,90" fill="var(--orange-deep)" opacity="0.5"/>
      <polygon class="centre-field" points="309,0 650,0 603,200 356,200" fill="var(--panel)"/>
      <polygon class="band band--right" points="650,0 808,0 650,200 603,200" fill="url(#band-tone)"/>
      <polygon class="band-shade band-shade--right" points="650,0 700,0 636,90" fill="var(--orange-deep)" opacity="0.5"/>
      <polygon class="pattern pattern--right" role="img" aria-label="Subtle abstract background pattern of embossed light-grey geometric squares"
               points="808,0 1000,0 1000,200 650,200" fill="url(#pattern-tone)"/>
      <polygon class="wedge wedge--right" points="1000,40 1000,200 915,200" fill="var(--dark-wedge)"/>
    </svg>

    <div class="billboard__content">
      <div class="brand">
        <span class="brand__square"></span>
        <span class="brand__name">Velmora</span>
      </div>
      <p class="tagline">Izvođenje i vođenje građevinskih radova</p>
      <span class="divider"></span>
      <p class="website">www.velmora.hr</p>
    </div>
  </div>
</body>
</html>
```